Birthday Card for Employees*

I'd like a birthday card designed using company logo to be given to employees

Colors

Designer to choose colors to be used in the design.

Requirements
Must have
• KWR Logos

```html
<!DOCTYPE html>
<html lang="en">
<head>
<meta charset="utf-8">
<title>Happy Birthday from KWR Solutions</title>
<link rel="stylesheet" href="https://fonts.googleapis.com/css2?family=Kaushan+Script&family=Open+Sans:wght@400;700&display=swap">
<style>
  :root {
    --bg-light: #f4f4f4;
    --bg-mid: #e9e9ea;
    --ink-grey: #77797c;
    --balloon-teal: #2fb3cc;
    --balloon-white: #dcdcdc;
    --ribbon-gold: #e2b33c;
  }
  html, body {
    margin: 0;
    padding: 0;
    overflow: hidden;
  }
  .card {
    position: relative;
    width: 1200px;
    height: 1200px;
    overflow: hidden;
    background: radial-gradient(ellipse at 50% 40%, var(--bg-light) 0%, var(--bg-mid) 100%);
  }
  .party-decor {
    position: absolute;
    left: 0;
    top: 0;
    width: 1200px;
    height: 680px;
  }
  .greeting {
    position: absolute;
    left: 0;
    top: 0;
    width: 1200px;
    height: 1200px;
  }
  .greeting text {
    font-family: "Kaushan Script", cursive;
    fill: var(--ink-grey);
  }
  .signoff {
    position: absolute;
    left: 154px;
    top: 1030px;
    display: flex;
    align-items: baseline;
    gap: 38px;
    font-family: "Open Sans", sans-serif;
    color: var(--ink-grey);
    line-height: 1;
  }
  .signoff-from {
    font-size: 72px;
    font-weight: 400;
    letter-spacing: 2px;
  }
  .company-name {
    font-size: 62px;
    font-weight: 700;
    letter-spacing: 1px;
  }
</style>
</head>
<body>
  <main class="card">
    <svg class="party-decor" viewBox="0 0 1200 680" role="img" aria-label="Teal, white and glitter balloons with gold and grey curling ribbons and confetti falling from the top">
      <defs>
        <linearGradient id="decorFade" x1="0" y1="0" x2="0" y2="1">
          <stop offset="0" stop-color="#5cc3d6"/>
          <stop offset="0.35" stop-color="#a9dbe4"/>
          <stop offset="0.65" stop-color="#d6dadb"/>
          <stop offset="1" stop-color="#ececec" stop-opacity="0"/>
        </linearGradient>
      </defs>
      <rect x="0" y="0" width="1200" height="680" fill="url(#decorFade)"/>
    </svg>

    <svg class="greeting" viewBox="0 0 1200 1200">
      <text x="44" y="610" font-size="200" textLength="460" lengthAdjust="spacingAndGlyphs">Happy</text>
      <text x="58" y="918" font-size="330" textLength="1090" lengthAdjust="spacingAndGlyphs">Birthday</text>
    </svg>

    <div class="signoff">
      <span class="signoff-from">FROM</span>
      <span class="company-name">KWR SOLUTIONS</span>
    </div>
  </main>
</body>
</html>
```